Corporate Design für aktuarielle Beratung
Zielgruppe
Wir sind eine aktuarielle Beratungsgesellschaft. Wir beraten und unterstützen in erster Linie Versicherungsunternehmen bei IT und Fachthemen mit Konzeptionierung, Programmierung und Testen.
Aufgabenstellung
Wir suchen ein hochwertiges Design, welches unseren Businesskunden, Professionalität, Zielorientiertheit, Authentizität, aber auch ein gewisses Maß an Kreativität wiederspiegelt. Hierbei darf es gerne eine Verknüpfung von klassisch und modern sein, da wir etwas frischen Wind in die sehr traditionellen Branche bringen und uns selbst als 'etwas anders' als unsere Wettbewerber wahrnehmen.

```html
<!DOCTYPE html>
<html lang="de">
<head>
<meta charset="utf-8">
<title>Quellenbrink Solutions – Briefbogen</title>
<link href="https://fonts.googleapis.com/css2?family=Montserrat:wght@300;400;500;600;700&family=Arimo:wght@400&display=swap" rel="stylesheet">
<style>
  :root {
    --backdrop: #d9d9d9;
    --paper: #f7f7f6;
    --ink: #1a1a1a;
    --ink-soft: #3a3a3a;
    --brand: #1d4a52;
    --rule: #2a2a2a;
    --sig-tone: #cfcfcf;
  }
  * { margin: 0; padding: 0; box-sizing: border-box; }
  html, body {
    width: 1200px; height: 880px; overflow: hidden;
    background: var(--backdrop);
  }
  .letterhead {
    position: absolute; left: 296px; top: 14px;
    width: 608px; height: 850px;
    background: var(--paper);
    box-shadow: 0 2px 10px rgba(0,0,0,0.12);
    font-family: 'Montserrat', sans-serif;
    color: var(--ink);
  }
  .brand {
    position: absolute; right: 46px; top: 58px;
    display: flex; align-items: center; gap: 8px;
    font-family: 'Montserrat', sans-serif;
    font-weight: 600; font-size: 16px; color: var(--brand);
    white-space: nowrap;
  }
  .brand-square { width: 14px; height: 14px; background: var(--brand); }
  .sender-line {
    position: absolute; left: 75px; top: 136px;
    font-size: 6.6px; font-weight: 600; color: var(--brand);
    text-decoration: underline; white-space: nowrap;
  }
  .recipient {
    position: absolute; left: 76px; top: 147px;
    font-style: normal;
    font-size: 10px; line-height: 10.5px; color: var(--ink-soft);
  }
  .contact-card {
    position: absolute; left: 412px; top: 135px;
    font-size: 8.6px; line-height: 9px; color: var(--ink-soft);
    white-space: nowrap;
  }
  .contact-name { font-size: 13px; font-weight: 600; color: var(--ink); line-height: 13px; }
  .contact-role { margin-bottom: 5px; }
  .contact-row { display: flex; }
  .contact-row span:first-child { width: 26px; }
  .subject {
    position: absolute; left: 75px; top: 294px;
    font-size: 19px; font-weight: 500;
  }
  .body-copy {
    position: absolute; left: 75px; top: 342px; width: 448px;
    font-family: 'Arimo', sans-serif; font-size: 11px; line-height: 12.2px;
  }
  .body-copy p { margin-bottom: 12px; }
  .closing {
    position: absolute; left: 74px; top: 508px;
    font-family: 'Arimo', sans-serif; font-size: 11px;
  }
  .signature {
    position: absolute; left: 74px; top: 530px;
    width: 132px; height: 28px;
    background: linear-gradient(90deg, var(--sig-tone), #e6e6e6);
  }
  .footer {
    position: absolute; left: 84px; top: 795px; width: 428px;
    border-top: 1px solid var(--rule);
    font-size: 6.3px; line-height: 6.8px; font-weight: 500; color: var(--ink-soft);
  }
  .footer-col { position: absolute; top: 7px; white-space: nowrap; }
  .footer-col.company { left: 0; }
  .footer-col.reach { left: 107px; }
  .footer-col.bank { left: 234px; }
  .footer-col.tax { left: 357px; }
</style>
</head>
<body>
  <main class="letterhead">
    <div class="brand"><span class="brand-square"></span>Quellenbrink Solutions</div>

    <div class="sender-line">Quellenbrink Solutions &nbsp;|&nbsp; Lindenweg 5, 10117 Berlin</div>
    <address class="recipient">
      Brandtner GmbH<br>Herrn Lukas Brandtner<br>12345 Obertal
    </address>

    <div class="contact-card">
      <div class="contact-name">Jonas Feldhaus</div>
      <div class="contact-role">CEO Quellenbrink Solutions</div>
      <div class="contact-row"><span>fon:</span><span>0471203040</span></div>
      <div class="contact-row"><span>fax:</span><span>0471203041</span></div>
      <div class="contact-row"><span>mail:</span><span>j.feldhaus@quellenbrink.de</span></div>
    </div>

    <h1 class="subject">Anliegen</h1>

    <div class="body-copy">
      <p>Sehr geehrte Damen und Herren,</p>
      <p>Gerne möchte ich Ihnen hiermit das neue Design des Unternehmens "Quellenbrink Solutions" vorstellen. Es handelt sich um ein Beratungsunternehmen für Versicherungsunternehmen mit Spezialisierung auf IT-Fragen. Das Design greift eine klare und moderne Designsprache auf. Getreu dem Motto "weniger ist mehr". Es finden sich keine aufdringlichen Farben oder verspielten Schriften, sondern klare, serifenlose Typografien sowie gesetzte Farben.</p>
      <p>Für Rückmeldungen, Änderungswünsche oder Kritk bin ich offen und freue mich auf Ihre Meinung.</p>
    </div>

    <div class="closing">Mit freundlichen Grüßen,</div>
    <div class="signature" role="img" aria-label="Handschriftliche Unterschrift von Jonas Feldhaus"></div>

    <footer class="footer">
      <div class="footer-col company">Quellenbrink Solutions<br>Inh.: Jonas Feldhaus<br>Lindenweg 12<br>10117 Berlin</div>
      <div class="footer-col reach">Tel.: 04712030400<br>E-Mail: info@quellenbrink.de<br>Web: www.quellenbrink.de</div>
      <div class="footer-col bank">Spreebank Berlin<br>BLZ: 123 4567 89<br>IBAN: 1234567890<br>KTO inh.: Jonas Feldhaus</div>
      <div class="footer-col tax">Steuer-Nr.: 12345678<br>Finanzamt Berlin</div>
    </footer>
  </main>
</body>
</html>
```